Financial PR company Homepage and Inner Page design

Please design a web homepage and innerpage for OVIN Public Relations.
OVIN Public Relations is a Financial PR company targeting Shenzhen Qian Special Economical Zone.
Note:
1. Menu includes ( Please specialize in Chinese and we want to see the Chinese fonts)
关于我们/服务板块/专业优势/合作伙伴/前海商圈/公司新闻/加盟我们/联系我们

2. Please refer to world class PR Business company and contribute your idea on website design and color themes.

3. We have attached the Logo for reference.

4. Anytime use picture for reference, please select asian business people pictures.

Cheers,

HI Designers, Thanks for the design submission. Here is our client feedback: 1. Adopt one screen design. 2. Use amiable Asia Business woman pictures. 3. Use contrastive color theme for the design. Cheers, Kip From TW

```html
<!DOCTYPE html>
<html lang="zh-CN">
<head>
<meta charset="utf-8">
<title>OVIN Public Relations</title>
<link href="https://fonts.googleapis.com/css2?family=Source+Sans+3:wght@400;600;700&family=Noto+Sans+SC:wght@400;500&display=swap" rel="stylesheet">
<style>
  :root {
    --ink: #ffffff;
    --logo-bg: #0d1a28;
    --logo-blue: #5ab8ea;
    --nav-bg: rgba(96, 112, 124, 0.82);
    --footer-bg: #0b0b0c;
    --footer-text: #8a8d90;
    --icon: #9a9da0;
  }
  * { box-sizing: border-box; margin: 0; padding: 0; }
  html, body { width: 1200px; height: 675px; overflow: hidden; background: #000; }
  body { font-family: "Source Sans 3", "Noto Sans SC", sans-serif; color: var(--ink); }
  .page { position: relative; width: 1200px; height: 675px; overflow: hidden; }
  .hero-photo {
    position: absolute; inset: 0 0 53px 0;
    background:
      radial-gradient(ellipse 45% 30% at 60% 78%, rgba(214,150,60,0.55), transparent 70%),
      radial-gradient(ellipse 30% 20% at 25% 85%, rgba(190,130,60,0.35), transparent 70%),
      linear-gradient(180deg, #e9e6e0 0%, #b9cfdc 14%, #5f8fb2 26%, #52697a 36%, #3b4a55 48%, #4a4a48 62%, #5b4f3f 78%, #3c3428 100%);
  }
  .hero-photo::after {
    content: ""; position: absolute; inset: 0;
    background: linear-gradient(90deg, rgba(255,240,220,0.25) 0%, transparent 40%, rgba(30,110,170,0.25) 100%);
  }
  .brand {
    position: absolute; left: 108px; top: 0; width: 271px; height: 102px;
    background: var(--logo-bg); border-radius: 0 0 8px 8px;
    display: flex; align-items: center; gap: 28px; padding-left: 42px;
  }
  .brand-dot { width: 36px; height: 36px; border-radius: 50%; background: var(--logo-blue); flex: none; }
  .brand-text { width: 121px; }
  .brand-name { font-size: 30px; font-weight: 400; line-height: 1; color: var(--ink); }
  .brand-tag { font-size: 15.5px; font-weight: 400; color: var(--ink); line-height: 1.05; margin-top: 1px; }
  .brand-cn { font-family: "Noto Sans SC", sans-serif; font-size: 11px; color: var(--logo-blue); text-align: right; margin-top: 2px; }
  .main-nav {
    position: absolute; left: 458px; top: 52px; width: 626px; height: 43px;
    background: var(--nav-bg); border-radius: 4px;
    display: flex; align-items: center; justify-content: center; gap: 19px;
  }
  .main-nav a { font-family: "Noto Sans SC", sans-serif; color: var(--ink); text-decoration: none; font-size: 14px; }
  .hero-copy { position: absolute; left: 0; right: 0; top: 237px; text-align: center; }
  .hero-title { font-size: 45px; font-weight: 700; line-height: 44px; letter-spacing: -0.8px; text-shadow: 0 1px 3px rgba(0,0,0,0.3); }
  .hero-text { font-size: 14.8px; line-height: 21px; margin-top: 9px; color: var(--ink); }
  .learn-more { display: inline-block; margin-top: 17px; font-size: 15px; font-weight: 700; color: var(--ink); text-decoration: none; }
  .site-footer {
    position: absolute; left: 0; right: 0; bottom: 0; height: 53px; background: var(--footer-bg);
    display: flex; align-items: center; justify-content: space-between; padding: 0 104px 0 109px;
    font-size: 13px; color: var(--footer-text);
  }
  .footer-right { display: flex; align-items: center; gap: 30px; }
  .social { display: flex; gap: 12px; }
  .social span { width: 16px; height: 16px; border-radius: 50%; background: var(--icon); display: block; }
</style>
</head>
<body>
<div class="page">
  <div class="hero-photo" role="img" aria-label="Aerial dusk view of a city skyline with lit highways and towers beside the sea"></div>

  <div class="brand">
    <span class="brand-dot"></span>
    <div class="brand-text">
      <div class="brand-name">OVIN PR</div>
      <div class="brand-tag">qianhai pr experts</div>
      <div class="brand-cn">前海欧文公关</div>
    </div>
  </div>

  <nav class="main-nav">
    <a href="#">关于我们</a><a href="#">服务板块</a><a href="#">专业优势</a><a href="#">合作伙伴</a><a href="#">前海商圈</a><a href="#">公司新闻</a><a href="#">加盟我们</a><a href="#">联系我们</a>
  </nav>

  <section class="hero-copy">
    <h1 class="hero-title">Welcome to<br>OVIN Public Relations</h1>
    <p class="hero-text">Lorem ipsum dolor sit amet, consectetur adipisicing elit, sed do eiusmod tempor incididunt ut labore et dolore magna aliqua.<br>Lorem ipsum dolor sit amet, consectetur adipisicing elit, sed do eiusmod tempor.</p>
    <a class="learn-more" href="#">LEARN MORE &gt;&gt;</a>
  </section>

  <footer class="site-footer">
    <div>Tel: +66 5550 1274 &nbsp;•&nbsp; Email: info@ovinpr.com</div>
    <div class="footer-right">
      <span>Copyright @ 2014. OVINPR.</span>
      <div class="social" aria-label="Social links"><span></span><span></span></div>
    </div>
  </footer>
</div>
</body>
</html>
```